Moravel Stenwick Inc needs a business card design

Looking for a unique, classy and sharp business card design.

Contact Information for Business Card

Moravel Stenwick Inc.
Marisa Ortega Bellido BScOT(c)
Occupational Therapist
(780) 555-0142
moravelstenwick@postlynx.net

```html
<!DOCTYPE html>
<html lang="en">
<head>
<meta charset="utf-8">
<title>Moravel Stenwick Inc. — Business Card</title>
<link href="https://fonts.googleapis.com/css2?family=Exo:wght@400;500;600;700&display=swap" rel="stylesheet">
<style>
  :root {
    --page-bg: #ffffff;
    --card-bg: #ffffff;
    --brand-green: #8cc63f;
    --brand-purple: #93278f;
    --ink: #231f20;
  }
  html, body {
    margin: 0;
    padding: 0;
    width: 1200px;
    height: 1200px;
    overflow: hidden;
    background: var(--page-bg);
    font-family: "Exo", sans-serif;
  }
  .card {
    position: absolute;
    left: 50px;
    top: 285px;
    width: 1100px;
    height: 630px;
    background: var(--card-bg);
    outline: 1px solid #ececec;
  }
  .brand {
    position: absolute;
    left: 85px;
    top: 280px;
    width: 380px;
    display: flex;
    align-items: center;
    gap: 14px;
  }
  .brand-dot {
    width: 22px;
    height: 22px;
    border-radius: 50%;
    background: var(--brand-purple);
    flex: none;
  }
  .brand-name {
    font-size: 33px;
    font-weight: 700;
    color: var(--brand-purple);
    line-height: 1;
    white-space: nowrap;
  }
  .divider {
    position: absolute;
    left: 549px;
    top: 172px;
    width: 4px;
    height: 285px;
    background: var(--brand-purple);
  }
  .person {
    position: absolute;
    left: 581px;
    top: 218px;
    width: 500px;
  }
  .person-name {
    margin: 0;
    font-size: 35px;
    font-weight: 600;
    color: var(--brand-green);
    line-height: 1;
    white-space: nowrap;
  }
  .credentials {
    font-size: 27px;
    font-weight: 700;
  }
  .person-title {
    margin: 10px 0 0 96px;
    font-size: 27px;
    font-weight: 500;
    color: var(--ink);
    line-height: 1;
  }
  .contact {
    position: absolute;
    left: 581px;
    top: 330px;
    list-style: none;
    margin: 0;
    padding: 0;
  }
  .contact-item {
    display: flex;
    align-items: center;
    height: 44px;
    font-size: 28px;
    font-weight: 500;
    color: var(--ink);
    white-space: nowrap;
  }
  .contact-icon {
    width: 32px;
    height: 30px;
    margin-right: 15px;
    flex: none;
  }
  .accent { color: var(--brand-green); }
</style>
</head>
<body>
  <main class="card">
    <div class="brand">
      <span class="brand-dot"></span>
      <span class="brand-name">Moravel Stenwick Inc.</span>
    </div>

    <div class="divider"></div>

    <section class="person">
      <h1 class="person-name">Marisa Ortega Bellido <span class="credentials">BScOT(c)</span></h1>
      <p class="person-title">Occupational Therapist</p>
    </section>

    <ul class="contact">
      <li class="contact-item">
        <svg class="contact-icon" viewBox="0 0 24 24" aria-hidden="true">
          <path fill="#8cc63f" d="M6.6 2.5c.6-.4 1.4-.2 1.8.4l2 3.2c.4.6.2 1.3-.3 1.7l-1.4 1c.9 2.2 2.6 4 4.7 5l1-1.4c.4-.5 1.2-.7 1.7-.3l3.2 2c.6.4.8 1.2.4 1.8l-1 1.6c-.6 1-1.8 1.5-3 1.2C10 17.6 5.7 13.2 4.1 7.4c-.3-1.1.1-2.3 1.1-3z"/>
        </svg>
        <span>(780) 555<span class="accent">-</span>0142</span>
      </li>
      <li class="contact-item">
        <svg class="contact-icon" viewBox="0 0 32 24" aria-hidden="true">
          <rect x="1" y="3" width="30" height="19" fill="#8cc63f"/>
          <path d="M1 3 L16 14 L31 3 M1 22 L12 11 M31 22 L20 11" fill="none" stroke="#ffffff" stroke-width="1.6"/>
        </svg>
        <span>moravelstenwick@postlynx<span class="accent">.</span>net</span>
      </li>
    </ul>
  </main>
</body>
</html>
```